FinTech company looking to revamp and expand client-facing interface for our financial models

Halvern Ledgerworks currently has a very simple website that allows clients to interact with our financial models. We are looking to completely redesign the current site and add several extra pages to provide extra functionality. We want the design to have a modern, slick feel, that will work on both a desktop or a tablet. It should be straightforward for clients to move between different pages at any time, and clear from the layout how to interact with the more advanced features. We have included screenshots of existing pages in the attached design brief, as well as sketches of the functionality required by the new pages, but can't provide a direct link to the current site.
Target Market(s)
Professional investors that will be paying to access the interface
Industry/Entity Type
Finance
Number of Pages Required
4 page
Colors
Designer to choose colors to be used in the design.
Look and feel
Each slider illustrates characteristics of the customer's brand and the style your logo design should communicate.

```html
<!DOCTYPE html>
<html lang="en">
<head>
<meta charset="utf-8">
<title>Halvern Ledgerworks – Model Interface</title>
<link rel="stylesheet" href="https://fonts.googleapis.com/css2?family=Roboto:wght@400;500;700;900&family=Open+Sans:wght@400;600&display=swap">
<style>
  :root{
    --page-bg:#ffffff;
    --wash:#e4f0f5;
    --bar-top:#40c4f4;
    --bar-bottom:#1787c0;
    --tab-active:#1a8cc6;
    --row-tint:#b7e6fa;
    --row-plain:#ffffff;
    --footer:#0e83ba;
    --ink:#1f2226;
    --link:#1a7db6;
    --field-border:#2d8fc6;
    --white:#ffffff;
  }
  *{box-sizing:border-box;margin:0;padding:0}
  html,body{width:693px;height:1200px;overflow:hidden;background:var(--page-bg)}
  body{position:relative;font-family:"Open Sans",Arial,sans-serif;color:var(--ink)}
  .backdrop{position:absolute;inset:0;z-index:0}
  .page-title{position:absolute;top:70px;left:0;width:100%;text-align:center;
    font-family:"Roboto",Arial,sans-serif;font-weight:900;font-size:30px;letter-spacing:.5px;z-index:1}

  .screen{position:absolute;background:var(--white);box-shadow:0 1px 6px rgba(0,0,0,.25);z-index:1;display:flex;flex-direction:column}
  .screen--models{left:16px;top:180px;width:660px;height:384px}
  .screen--factors{left:46px;top:640px;width:600px;height:384px}

  .app-bar{height:36px;background:linear-gradient(var(--bar-top),var(--bar-bottom));display:flex;align-items:stretch;color:var(--white);font-family:"Roboto",Arial,sans-serif}
  .brand{font-weight:700;font-size:15px;display:flex;align-items:center;letter-spacing:.3px}
  .screen--models .brand{width:212px;padding-left:79px}
  .screen--factors .brand{width:197px;padding-left:72px}
  .index-tabs{display:flex}
  .index-tabs a{color:var(--white);text-decoration:none;font-size:9.5px;display:flex;align-items:center;padding:0 8px}
  .index-tabs a.is-active{background:var(--tab-active)}
  .screen--models .index-tabs a.is-active{padding:0 9px}
  .main-nav{margin-left:auto;display:flex;align-items:center;gap:5px;font-size:8.5px;padding-right:38px}
  .main-nav span{display:flex;align-items:center;gap:4px;margin-left:5px}
  .main-nav svg{width:10px;height:10px;fill:var(--white)}

  .filters{padding:25px 0 0 79px;height:97px;font-size:8.2px;font-weight:600}
  .screen--factors .filters{padding:30px 0 0 75px;height:126px}
  .filter-row{display:flex;align-items:center;height:21px}
  .screen--factors .filter-row{height:19px}
  .filter-row label{width:81px}
  .screen--factors .filter-row label{width:75px}
  .filter-row .field{width:86px;height:13px;border:1px solid var(--field-border);font-size:8px;padding-left:4px;line-height:11px;font-weight:400}
  .screen--factors .filter-row .field{width:78px;height:12px;line-height:10px}
  .export{display:flex;align-items:center;gap:5px;color:var(--link);font-size:8.2px;margin-top:6px;font-weight:400}
  .export svg{width:10px;height:10px}

  .data-table{width:100%;border-collapse:collapse;table-layout:fixed;text-align:center}
  .data-table th{height:33px;background:linear-gradient(var(--bar-top),var(--bar-bottom));color:var(--white);font-family:"Roboto",Arial,sans-serif;font-weight:500;font-size:9px}
  .data-table td{font-size:7.6px;line-height:9px;height:35px}
  .screen--factors .data-table th{height:30px}
  .screen--factors .data-table td{height:31px;font-size:7.2px}
  .data-table tbody tr:nth-child(odd){background:var(--row-tint)}
  .data-table tbody tr:nth-child(even){background:var(--row-plain)}
  .sort{font-size:7px;margin-left:3px}

  .app-footer{margin-top:auto;height:18px;background:var(--footer);color:var(--white);font-size:7px;display:flex;align-items:center;padding-left:26px}
  .screen--factors .app-footer{padding-left:24px}
</style>
</head>
<body>

<svg class="backdrop" width="693" height="1200" viewBox="0 0 693 1200" aria-hidden="true">
  <path d="M693 20 C620 140 560 260 520 360 C500 420 500 470 540 520 L693 520 Z" fill="var(--wash)"/>
  <path d="M0 990 C60 995 120 1010 160 1060 C190 1100 205 1150 215 1200 L0 1200 Z" fill="var(--wash)"/>
  <path d="M693 1040 C640 1080 600 1140 590 1200 L693 1200 Z" fill="var(--wash)"/>
</svg>

<h1 class="page-title">HALVERN</h1>

<section class="screen screen--models">
  <header class="app-bar">
    <div class="brand">HALVERN</div>
    <nav class="index-tabs"><a class="is-active">QBASE</a><a>2500</a><a>830</a><a>420</a></nav>
    <nav class="main-nav">
      <span><svg viewBox="0 0 10 10"><path d="M5 1 0.5 5H2v4h2.3V6.5h1.4V9H8V5h1.5z"/></svg>Models</span>
      <span><svg viewBox="0 0 10 10"><g fill="none" stroke="#fff" stroke-width=".8"><ellipse cx="5" cy="5" rx="4.4" ry="1.6"/><ellipse cx="5" cy="5" rx="4.4" ry="1.6" transform="rotate(60 5 5)"/><ellipse cx="5" cy="5" rx="4.4" ry="1.6" transform="rotate(-60 5 5)"/></g><circle cx="5" cy="5" r=".9"/></svg>Sensitivities</span>
      <span><svg viewBox="0 0 10 10"><path d="M5 .5 6.4 3.6 9.7 3.9 7.2 6.1 7.9 9.4 5 7.7 2.1 9.4 2.8 6.1.3 3.9 3.6 3.6z"/></svg>Favourites</span>
    </nav>
  </header>

  <form class="filters">
    <div class="filter-row"><label>Quality&nbsp; Threshold:</label><div class="field">-10</div></div>
    <div class="filter-row"><label>Abs. sat&nbsp; Threshold:</label><div class="field">-10</div></div>
    <div class="export"><svg viewBox="0 0 10 10" fill="none" stroke="#1f2226" stroke-width="1.1"><path d="M4 2H1v7h7V6"/><path d="M5.5 1H9v3.5M9 1 4.5 5.5"/></svg>EXPORT</div>
  </form>

  <table class="data-table">
    <colgroup><col style="width:48px"><col style="width:48px"><col style="width:54px"><col style="width:50px"><col><col><col><col><col><col><col><col></colgroup>
    <thead><tr><th>ID<span class="sort">&#8964;</span></th><th>Sector</th><th>Time</th><th>Quality</th><th>Stat 1</th><th>Stat 2</th><th>Stat 3</th><th>Stat 4</th><th>Stat 5</th><th>Stat 6</th><th>Stat 7</th><th>Stat 8</th></tr></thead>
    <tbody>
      <tr><td>Model 1</td><td>Materials</td><td>2019-07-03<br>12:15:00.000</td><td>30.2288</td><td>2.01574</td><td>23.305</td><td>-0.149368</td><td>22.3054</td><td>4.63714</td><td>0.945706</td><td>2.81949</td><td>2.60858</td></tr>
      <tr><td>Model 2</td><td>Industrials</td><td>2019-07-03<br>12:15:00.000</td><td>32.8694</td><td>0.87307</td><td>32.185</td><td>-0.0336927</td><td>33.9911</td><td>11.5693</td><td>-0.472968</td><td>-0.830458</td><td>6.80646</td></tr>
      <tr><td>Model 3</td><td>Consumer<br>Discretionary</td><td>2019-07-03<br>12:15:00.000</td><td>1.66002</td><td>-0.569222</td><td>159.814</td><td>0.0252328</td><td>172.616</td><td>10.2875</td><td>-0.750396</td><td>-0.385309</td><td>4.69146</td></tr>
      <tr><td>Model 4</td><td>Information<br>Technology</td><td>2019-07-03<br>12:15:00.000</td><td>45.6856</td><td>0.412148</td><td>202.488</td><td>0.00849232</td><td>205.834</td><td>11.9094</td><td>-0.137913</td><td>0.449595</td><td>3.85106</td></tr>
      <tr><td>Model 5</td><td>Information<br>Technology</td><td>2019-07-03<br>12:15:00.000</td><td>75.7733</td><td>7.06728</td><td>188.605</td><td>0.016913</td><td>181.665</td><td>3.82241</td><td>0.981019</td><td>1.29847</td><td>3.34927</td></tr>
    </tbody>
  </table>

  <footer class="app-footer">Copyright © 2019 Halvern Ledgerworks - All Rights Reserved.</footer>
</section>

<section class="screen screen--factors">
  <header class="app-bar">
    <div class="brand">HALVERN</div>
    <nav class="index-tabs"><a class="is-active">QBASE</a><a>2500</a><a>830</a><a>420</a></nav>
    <nav class="main-nav">
      <span><svg viewBox="0 0 10 10"><path d="M5 1 0.5 5H2v4h2.3V6.5h1.4V9H8V5h1.5z"/></svg>Models</span>
      <span><svg viewBox="0 0 10 10"><g fill="none" stroke="#fff" stroke-width=".8"><ellipse cx="5" cy="5" rx="4.4" ry="1.6"/><ellipse cx="5" cy="5" rx="4.4" ry="1.6" transform="rotate(60 5 5)"/><ellipse cx="5" cy="5" rx="4.4" ry="1.6" transform="rotate(-60 5 5)"/></g><circle cx="5" cy="5" r=".9"/></svg>Sensitivities</span>
      <span><svg viewBox="0 0 10 10"><path d="M5 .5 6.4 3.6 9.7 3.9 7.2 6.1 7.9 9.4 5 7.7 2.1 9.4 2.8 6.1.3 3.9 3.6 3.6z"/></svg>Favourites</span>
    </nav>
  </header>

  <form class="filters">
    <div class="filter-row"><label>Stat 1 Threshold</label><div class="field">-10</div></div>
    <div class="filter-row"><label>Stat 2 Threshold</label><div class="field">-10</div></div>
    <div class="filter-row"><label>Stat 2 Threshold</label><div class="field">-10</div></div>
    <div class="export"><svg viewBox="0 0 10 10" fill="none" stroke="#1f2226" stroke-width="1.1"><path d="M4 2H1v7h7V6"/><path d="M5.5 1H9v3.5M9 1 4.5 5.5"/></svg>EXPORT</div>
  </form>

  <table class="data-table">
    <colgroup><col style="width:84px"><col style="width:54px"><col style="width:62px"><col style="width:64px"><col style="width:52px"><col style="width:72px"><col style="width:62px"><col style="width:88px"><col></colgroup>
    <thead><tr><th>Factor</th><th>IDS</th><th>Sector</th><th>Stat 1</th><th>Stat 2</th><th>Stat 3</th><th>Stat 4</th><th>Stat 5</th><th>Stat 6</th></tr></thead>
    <tbody>
      <tr><td>Factor 1</td><td>Model 1</td><td>Materials</td><td>-1.4</td><td>0.1</td><td>-3.1</td><td>0.7</td><td>30.2</td><td>0.9</td></tr>
      <tr><td>Factor 2</td><td>Model 1</td><td>Materials</td><td>2.8</td><td>0.1</td><td>6.1</td><td>100</td><td>30.2</td><td>0.9</td></tr>
      <tr><td>Factor 3</td><td>Model 1</td><td>Materials</td><td>-3.7</td><td>2.7</td><td>-7.2</td><td>100</td><td>30.2</td><td>0.9</td></tr>
      <tr><td>Factor 1</td><td>Model 2</td><td>Industrials</td><td>2.8</td><td>0.2</td><td>2.7</td><td>0.5</td><td>32.9</td><td>-0.5</td></tr>
      <tr><td>Factor 2</td><td>Model 2</td><td>Industrials</td><td>0.8</td><td>0.3</td><td>2.5</td><td>0.5</td><td>32.9</td><td>-0.5</td></tr>
    </tbody>
  </table>

  <footer class="app-footer">Copyright © 2019 Halvern Ledgerworks - All Rights Reserved.</footer>
</section>

</body>
</html>
```